Business Card for Academic Coach

I need a business card designed for me - a private tutor/academic coach.

Glen Marlowe
Academic Coach
AB Velden University, 1994 Cum Laude
Phone: 555-317-8842
glenmmarlowe@quillpost.example

Subjects
CRX and UPT
Math, Physics, Writing

Industry/Entity Type

Business

```html
<!DOCTYPE html>
<html lang="en">
<head>
<meta charset="utf-8">
<title>Glen Marlowe – Academic Coach Business Card</title>
<link rel="stylesheet" href="https://fonts.googleapis.com/css2?family=Roboto:wght@400;500;700&family=Roboto+Condensed:wght@400;700&display=swap">
<style>
  :root {
    --page-bg: #f4f4f4;
    --card-white: #ffffff;
    --card-white-shade: #ececec;
    --card-black: #151515;
    --card-black-deep: #0a0a0a;
    --brand-red: #d11f26;
    --brand-red-dark: #9e1318;
    --ink-dark: #1c1c1c;
    --ink-grey: #6f6f6f;
    --ink-light: #f2f2f2;
    --back-ring: #242424;
    --back-subtitle: #8a8a8a;
  }
  * { box-sizing: border-box; margin: 0; padding: 0; }
  html, body {
    width: 1200px; height: 900px; overflow: hidden;
    background: var(--page-bg);
  }
  .canvas {
    position: relative; width: 1200px; height: 900px;
    display: flex; align-items: center; justify-content: center; gap: 40px;
  }
  .card {
    position: relative; width: 540px; height: 309px;
    border-radius: 18px; overflow: hidden;
    box-shadow: 0 6px 18px rgba(0,0,0,0.18);
  }

  /* Front */
  .card-front { background: var(--card-black); }
  .front-top {
    position: absolute; left: 0; top: 0; width: 100%; height: 152px;
    background: linear-gradient(180deg, var(--card-white) 0%, var(--card-white-shade) 100%);
  }
  .identity {
    position: absolute; left: 24px; top: 44px;
    display: flex; align-items: center; gap: 16px;
  }
  .identity-dot {
    width: 72px; height: 72px; border-radius: 50%;
    background: var(--brand-red);
  }
  .identity-name {
    font-family: "Roboto", Arial, sans-serif; font-weight: 500;
    font-size: 34px; line-height: 1; color: var(--ink-dark);
  }
  .identity-role {
    margin-top: 8px;
    font-family: "Roboto Condensed", Arial, sans-serif; font-weight: 400;
    font-size: 13px; letter-spacing: 6.5px; color: var(--ink-grey);
  }
  .subject-band {
    position: absolute; left: 0; top: 152px; width: 100%; height: 19px;
    background: linear-gradient(180deg, var(--brand-red) 0%, var(--brand-red-dark) 100%);
    font-family: "Roboto Condensed", Arial, sans-serif; font-weight: 700;
    font-size: 12px; letter-spacing: 4px; line-height: 19px;
    color: var(--card-black-deep); padding-left: 34px; white-space: pre;
  }
  .front-bottom {
    position: absolute; left: 0; top: 171px; width: 100%; height: 138px;
    background: linear-gradient(180deg, var(--card-black) 0%, var(--card-black-deep) 100%);
  }
  .contact-list {
    position: absolute; left: 22px; top: 24px; list-style: none;
    font-family: "Roboto", Arial, sans-serif; font-size: 14px; color: var(--ink-light);
  }
  .contact-item { display: flex; align-items: center; gap: 7px; height: 20px; }
  .contact-icon { width: 12px; height: 12px; fill: var(--brand-red); flex: none; }

  /* Back */
  .card-back {
    background: radial-gradient(circle at 50% 40%, #1d1d1d 0%, var(--card-black) 55%, var(--card-black-deep) 100%);
  }
  .back-ring {
    position: absolute; left: 50%; top: 50%;
    width: 300px; height: 300px; margin: -150px 0 0 -150px;
    border-radius: 50%; border: 12px solid var(--back-ring);
  }
  .back-title {
    position: absolute; left: 0; top: 110px; width: 100%; text-align: center;
  }
  .back-name {
    font-family: "Roboto", Arial, sans-serif; font-weight: 500;
    font-size: 36px; line-height: 1; color: var(--brand-red);
  }
  .back-role {
    margin-top: 8px;
    font-family: "Roboto Condensed", Arial, sans-serif; font-weight: 400;
    font-size: 15px; letter-spacing: 7px; color: var(--back-subtitle);
  }
</style>
</head>
<body>
<main class="canvas">
  <section class="card card-front" aria-label="Business card front">
    <div class="front-top">
      <div class="identity">
        <div class="identity-dot"></div>
        <div>
          <div class="identity-name">Glen Marlowe</div>
          <div class="identity-role">ACADEMIC COACH</div>
        </div>
      </div>
    </div>
    <div class="subject-band">CRX AND UPT   MATH, PHYSICS, WRITING</div>
    <div class="front-bottom">
      <ul class="contact-list">
        <li class="contact-item">
          <svg class="contact-icon" viewBox="0 0 24 24" aria-hidden="true"><path d="M6.6 10.8c1.4 2.8 3.8 5.1 6.6 6.6l2.2-2.2c.3-.3.7-.4 1-.2 1.1.4 2.3.6 3.6.6.6 0 1 .4 1 1V20c0 .6-.4 1-1 1C10.6 21 3 13.4 3 4c0-.6.4-1 1-1h3.5c.6 0 1 .4 1 1 0 1.3.2 2.5.6 3.6.1.3 0 .7-.2 1L6.6 10.8z"/></svg>
          Phone: 555-317-8842
        </li>
        <li class="contact-item">
          <svg class="contact-icon" viewBox="0 0 24 24" aria-hidden="true"><path d="M2 5h20v14H2z M4 7v.5l8 5 8-5V7l-8 5z" fill-rule="evenodd"/></svg>
          glenmmarlowe@quillpost.example
        </li>
        <li class="contact-item">
          <svg class="contact-icon" viewBox="0 0 24 24" aria-hidden="true"><path d="M12 3 1 12h3v9h6v-6h4v6h6v-9h3z"/></svg>
          AB Velden University, 1994 Cum Laude
        </li>
      </ul>
    </div>
  </section>

  <section class="card card-back" aria-label="Business card back">
    <div class="back-ring"></div>
    <div class="back-title">
      <div class="back-name">Glen Marlowe</div>
      <div class="back-role">ACADEMIC COACH</div>
    </div>
  </section>
</main>
</body>
</html>
```